Orva Business Card

we need a business card for flooring business called Orva Flooring, the design should be black and white. we have 2 locations

Ashvale Showroom
527 Kellerman Road,
Ashvale VIC 3188

Corranbrook Showroom
462 Bramwell Hwy,
Corranbrook VIC 3217

email : sales@orvaflooring.com.au
(03) 9471 2830

Please inform we sell , Laminate, Hybrid, Timber, carpet and commercial flooring

```html
<!DOCTYPE html>
<html lang="en">
<head>
<meta charset="utf-8">
<title>Orva Flooring — Business Card</title>
<link href="https://fonts.googleapis.com/css2?family=Lato:ital,wght@0,300;0,400;0,700;0,900;1,700&display=swap" rel="stylesheet">
<style>
  :root{
    --stage:#3a3a3a;
    --card-dark:#1f1d1e;
    --card-light:#ffffff;
    --ink:#1a1a1a;
    --ink-soft:#4a4a4a;
    --line-light:#ffffff;
  }
  *{box-sizing:border-box;margin:0;padding:0}
  html,body{width:1200px;height:875px;overflow:hidden}
  body{
    background:var(--stage);
    font-family:"Lato",sans-serif;
    display:flex;align-items:center;justify-content:center;gap:40px;
  }
  .card{
    width:540px;height:310px;border-radius:26px;position:relative;
    box-shadow:0 14px 34px rgba(0,0,0,.45);
  }
  /* front */
  .card--front{background:var(--card-dark);color:var(--line-light)}
  .front-frame{
    position:absolute;inset:18px;border:2px solid var(--line-light);border-radius:16px;
  }
  .front-brand{
    position:absolute;left:0;right:0;top:78px;text-align:center;
    font-weight:300;color:var(--line-light);letter-spacing:.08em;
  }
  .front-brand .brand-name{display:block;font-size:72px;line-height:1}
  .front-brand .brand-sub{display:block;font-size:34px;margin-top:8px;letter-spacing:.12em}
  .tagline{
    position:absolute;left:44px;bottom:9px;padding:0 8px;
    background:var(--card-dark);font-size:13px;letter-spacing:.02em;white-space:nowrap;
  }
  .tagline strong{font-weight:700;font-style:italic}
  /* back */
  .card--back{background:var(--card-light);color:var(--ink);display:flex;align-items:center}
  .back-brand{
    width:250px;text-align:center;font-weight:300;color:var(--ink);letter-spacing:.08em;
  }
  .back-brand .brand-name{display:block;font-size:56px;line-height:1}
  .back-brand .brand-sub{display:block;font-size:26px;margin-top:8px;letter-spacing:.12em}
  .divider{width:2px;height:170px;background:var(--ink)}
  .details{padding-left:24px;font-size:12.5px;line-height:1.3;color:var(--ink-soft)}
  .person-name{font-size:22px;font-weight:900;color:var(--ink);letter-spacing:.01em;line-height:1.1}
  .person-role{font-size:14px;margin-bottom:8px}
  .showroom{margin-bottom:6px}
  .showroom-title{font-weight:700;color:var(--ink)}
  .contact-list{list-style:none;margin-top:4px}
  .contact-list li{display:flex;align-items:center;gap:7px}
  .contact-list svg{width:11px;height:11px;flex:none}
</style>
</head>
<body>

<section class="card card--front" aria-label="Card front">
  <div class="front-frame"></div>
  <div class="front-brand">
    <span class="brand-name">ORVA</span>
    <span class="brand-sub">FLOORING</span>
  </div>
  <p class="tagline"><strong>We Sell</strong>, Laminate, Hybrid, Timber, Carpet &amp; Commercial Flooring</p>
</section>

<section class="card card--back" aria-label="Card back">
  <div class="back-brand">
    <span class="brand-name">ORVA</span>
    <span class="brand-sub">FLOORING</span>
  </div>
  <div class="divider"></div>
  <div class="details">
    <p class="person-name">DANIEL HART</p>
    <p class="person-role">Founder &amp; CEO</p>
    <div class="showroom">
      <p class="showroom-title">Ashvale Showroom</p>
      <p>527 Kellerman Road,</p>
      <p>Ashvale VIC 3188</p>
    </div>
    <div class="showroom">
      <p class="showroom-title">Corranbrook Showroom</p>
      <p>462 Bramwell Hwy,</p>
      <p>Corranbrook VIC 3217</p>
    </div>
    <ul class="contact-list">
      <li><svg viewBox="0 0 24 24" aria-hidden="true"><path fill="#1a1a1a" d="M6.6 10.8a15 15 0 0 0 6.6 6.6l2.2-2.2a1 1 0 0 1 1-.25 11.4 11.4 0 0 0 3.6.57 1 1 0 0 1 1 1V20a1 1 0 0 1-1 1A17 17 0 0 1 3 4a1 1 0 0 1 1-1h3.5a1 1 0 0 1 1 1c0 1.25.2 2.45.57 3.57a1 1 0 0 1-.25 1z"/></svg>(03) 9471 2830</li>
      <li><svg viewBox="0 0 24 24" aria-hidden="true"><path fill="#1a1a1a" d="M2 5h20v14H2z"/><path fill="none" stroke="#fff" stroke-width="1.8" d="M2.5 5.5 12 13l9.5-7.5"/></svg>sales@orvaflooring.com.au</li>
      <li><svg viewBox="0 0 24 24" aria-hidden="true"><circle cx="12" cy="12" r="10" fill="#1a1a1a"/><path fill="none" stroke="#fff" stroke-width="1.4" d="M2 12h20M12 2c3 3 3 17 0 20M12 2c-3 3-3 17 0 20"/></svg>orvaflooring.com.au</li>
    </ul>
  </div>
</section>

</body>
</html>
```